Hurricane Damage Public Adjuster Billboard

I have created several projects with you and have several great designs. I need to format them into a Billboard for upcoming Hurricane Season. Need done in a month. Im also in process of getting an eye catching and easy to remember 800# Vanity phone number like Call 800-Stormfix or 800- Need Help? My included past Sketch Guild projects will give you an idea of what colors, schemes, and designs I gravitate towards. 3 past Design projects were 1) 2 Logos where I picked the 1st place and the 2nd place and 2) Index Card where I picked the winner as the Index Card and the 2nd place as a Post Card. Point is, I will pick and pay for 2 winners if they're good. This should help to sweeten the pot. Also, please look at my website for ideas that I like:

www.TheClaimWardenGroup.com
I want people to feel that I am the best and highest. Level.

I've been getting a lot of quick half effort designs basically cut & pasting my previous projects. Please don't rush and take your time to be creative. A an example, my Biggest Competitor is Crestline Public Adjusting. Their colors are Black and Gold while mine are Blue, White, and Black with a highlight of Orange if possible. I JUST imported a picture of their BillBoard. I need mine better and BLOW AWAY THEIRS. Terms like "Don't be Victimized Twice ?, Don't let the Hurricane Ruin your Life?". "Get Fairly Paid & Move On" "Our Clients Claims are VIP?
Updates

I'm getting a lot of quick half effort ones. I'd rather you take your time and really put some thoughts and effort into it. My Biggest Competitor is Crestline Public Adjusting. They have black & gold colors, while I have Blue, Black, and white.

It needs to blow theirs away. I have imported their Billboard for comparative purposes.

Guy's,
I'll make it easier for you in what I'm looking for. Please look at the Crestline Billboard picture attached.

1) Put my "Blue Shield" to the left, replacing their logo
2) change color patterns from their (Black, Gold, White) to my color schemes of (Black, Blue, White)
3) I want to see my name where their is:

THE
Claim Warden Group
EXPERT & LOCAL Public Adjusters
"FOR THE POLICYHOLDER!!"

4) to the right, add the A+Rated logo and QTR+ Accredited logo, 5 Star Zentrio Rated logo, 5 Start BLOCKLINK Highly Rated logo, etc..

5) the right side is where you can be creative as I will not have a picture of me there.

"20+ Years of Experience, Recovering Millions for our VIP Clients"

"Your Best, Locally-Based Private Adjuster & Advocate'
"FOR THE POLICYHOLDER!!"

"Don't be victimized Twice!!"

"Don't let the Hurricane Ruin Your Life!!"

This should really help. Also, refer to my website, maybe a couple testimonial fillers?

Thanks all,

marvin@TheClaimWardenGroup.com

Just imported a few awards that would look great to the right side with all the other 5 Star Ratings and accolades.
This right section could be titled like zmy Website:

5 Star Reviews, Ratings & Awards:
4-5 Logos underneath?

Target Market(s)

Coastal place where a Hurricane 🌀 🌀 Hits

Industry/Entity Type

Hurricane Public Insurance Adjuster

Font styles to use
Sans Serif
Other font styles liked:
• Calvera fonts

Colors
0054AA
0677BA
7BADD7
CADEEF
E8F1F8
EE7325
F08F49
F5BC92
FAE3D3
FDF4ED

Requirements
Must have
• Use my past project logos, colors, and schemes to create eye grabbing BillBoard
Nice to have
Should not have
• Not be too busy, must be Easy to Read, Eye Catchy

```html
<!DOCTYPE html>
<html lang="en">
<head>
<meta charset="utf-8">
<title>Claim Warden Group Billboard</title>
<link rel="stylesheet" href="https://fonts.googleapis.com/css2?family=Montserrat:wght@500;600;700;800;900&display=swap">
<style>
  :root {
    --canvas: #43434b;
    --board: #0b0c16;
    --board-glow: #3a2a24;
    --blue: #1aa3e8;
    --blue-deep: #0677ba;
    --white: #ffffff;
    --ink: #0b0c16;
    --red: #e8242a;
    --gold: #f4b400;
    --tag: #1f9bd6;
    --photo-a: #8f7bd6;
    --photo-b: #c8a07e;
  }
  html, body {
    margin: 0;
    width: 1166px;
    height: 1200px;
    overflow: hidden;
    background: var(--canvas);
    font-family: "Montserrat", sans-serif;
  }
  .billboard {
    position: absolute;
    left: 33px;
    top: 425px;
    width: 1200px;
    height: 349px;
    transform: scale(0.9167);
    transform-origin: 0 0;
    background:
      radial-gradient(ellipse 40% 60% at 30% 0%, rgba(90,60,50,.55), transparent 70%),
      radial-gradient(ellipse 30% 50% at 75% 10%, rgba(90,60,50,.5), transparent 70%),
      var(--board);
    color: var(--white);
    overflow: hidden;
  }
  .brand-mark {
    position: absolute;
    left: 38px; top: 95px;
    width: 140px;
    display: flex; flex-direction: column; align-items: center; gap: 10px;
  }
  .brand-mark .dot { width: 38px; height: 38px; background: var(--blue); }
  .brand-mark .name {
    color: var(--blue); font-weight: 800; font-size: 22px; line-height: 1.1; text-align: center;
  }
  .wordmark { position: absolute; left: 210px; top: 58px; width: 300px; text-align: center; }
  .wordmark .the {
    display: flex; align-items: center; justify-content: center; gap: 4px;
    font-weight: 800; font-size: 32px; line-height: 1;
  }
  .wordmark .the::before, .wordmark .the::after {
    content: ""; height: 2px; width: 100px; background: var(--white);
  }
  .wordmark .line1 { font-weight: 900; font-size: 30px; line-height: 1.15; margin-top: 2px; }
  .wordmark .line2 { font-weight: 900; font-size: 40px; line-height: 1.05; }
  .wordmark .tagline { font-weight: 600; font-size: 16.5px; margin-top: 6px; }
  .wordmark .policy { color: var(--blue); font-weight: 600; font-size: 22px; margin-top: 4px; letter-spacing: .3px; }
  .wordmark .email { font-size: 11px; font-weight: 500; letter-spacing: 1.3px; margin-top: 4px; }
  .divider { position: absolute; left: 545px; top: 140px; width: 2px; height: 52px; background: rgba(255,255,255,.6); }
  .pitch { position: absolute; left: 583px; top: 100px; }
  .pitch .headline { font-weight: 700; font-size: 20px; line-height: 25px; }
  .pitch .tag {
    display: inline-block; margin-top: 12px; background: var(--tag);
    font-size: 11px; font-weight: 800; color: var(--ink); padding: 2px 8px 1px 3px;
    clip-path: polygon(0 0, 100% 0, 92% 100%, 0 100%);
  }
  .pitch .phone { display: flex; align-items: center; gap: 4px; font-weight: 700; font-size: 34px; margin-top: 2px; }
  .photo {
    position: absolute; left: 795px; top: 15px; width: 370px; height: 247px;
    background: radial-gradient(ellipse 55% 70% at 50% 80%, var(--photo-a), transparent 75%),
                radial-gradient(ellipse 25% 30% at 52% 25%, var(--photo-b), transparent 80%);
  }
  .slogan-band {
    position: absolute; left: 0; top: 262px; width: 100%; height: 36px;
    background: var(--white); color: var(--ink);
    font-weight: 900; font-size: 28px; line-height: 36px; text-align: center; letter-spacing: .5px;
  }
  .footer { position: absolute; left: 48px; top: 306px; right: 44px; display: flex; align-items: center; }
  .footer .site { font-size: 25px; font-weight: 500; letter-spacing: .8px; flex: 1; }
  .ratings { display: flex; align-items: center; gap: 18px; }
  .rating-zentrio { text-align: center; line-height: 1; }
  .rating-zentrio .label { font-size: 17px; font-weight: 600; color: var(--white); }
  .rating-zentrio .stars { color: var(--gold); font-size: 10px; letter-spacing: 1px; }
  .badge-blocklink { width: 86px; height: 22px; border: 1px solid #888; background: #1a1a22; display: flex; }
  .badge-blocklink::before { content: ""; width: 20px; background: #e8731f; }
  .rating-aplus { color: var(--red); font-weight: 600; font-size: 24px; }
  .badge-qtr { width: 78px; height: 30px; background: #0d5a7c; border-radius: 3px; }
</style>
</head>
<body>
  <div class="billboard">
    <div class="brand-mark">
      <span class="dot"></span>
      <span class="name">Claim Warden Group</span>
    </div>

    <div class="wordmark">
      <div class="the">THE</div>
      <div class="line1">CLAIM WARDEN</div>
      <div class="line2">GROUP</div>
      <div class="tagline">EXPERT &amp; LOCAL Public Adjusters</div>
      <div class="policy">FOR THE POLICYHOLDER</div>
      <div class="email">marvin@TheClaimWardenGroup.com</div>
    </div>

    <div class="divider"></div>

    <div class="pitch">
      <div class="headline">DON'T LET THE<br>HURRICANE RUIN<br>YOUR LIFE</div>
      <div class="tag">CONTACT NOW</div>
      <div class="phone">
        <svg width="16" height="22" viewBox="0 0 16 22" aria-hidden="true">
          <path d="M6 2 C2 4 2 18 6 20 L8 16 C6 15 6 7 8 6 Z" fill="#fff"/>
        </svg>
        (555) 014-2290
      </div>
    </div>

    <div class="photo" role="img" aria-label="Photo of a worried homeowner in a lavender t-shirt holding his head"></div>

    <div class="slogan-band">YOUR BEST, LOCALLY-BASED PRIVATE ADJUSTER &amp; ADVOCATE</div>

    <div class="footer">
      <div class="site">www.TheClaimWardenGroup.com</div>
      <div class="ratings">
        <div class="rating-zentrio"><div class="label">Zentrio</div><div class="stars">★★★★★</div></div>
        <div class="badge-blocklink" role="img" aria-label="BLOCKLINK 5 star rating badge"></div>
        <div class="rating-aplus">A+ Rating</div>
        <div class="badge-qtr" role="img" aria-label="QTR+ accredited business badge"></div>
      </div>
    </div>
  </div>
</body>
</html>
```